Trindle Salve by Petal Wrens: All Natural Lip Balm Co. Looking for New Label

Greetings, our company is called Petal Wrens and we are a start-up founded in early 2014. We make 100% All-Natural lip balm, called Trindle Salve, in a variety of flavors and we are looking for a new label that incorporates part of our logo and highlights our product name and our lip balms flavor (see attached files). Our website is: trindlesalve.example, and we are on Twitter: @PetalWrensSalves, and Facebook: /PetalWrensSalves. Our lip balms are made with beeswax, sweet almond oil, shea butter, coconut oil and other all natural oils and flavors.

The design should be clean, and communicate comfort, its "all-natural-ness", reliability, and fun. The colors we would like to have incorporated are burgundy, a deep, but not dark orange (see files, website, logo, graphics), some green and maybe gold/yellow. Given that the lip balm tubes are small (standard tubes), we would like to assure that the lip balm name, the flavor, and part of the logo- (perhaps the bee), are clearly visible and easily read. I am open to a variety of fonts, as long as they convey what I have stated above.

We want to use the label graphics and our logo for not only labeling our product, but also for use on our website, on banners, signs, retail boxes, letterhead, tee shirts, etc. If we like the design we are open to working with you again as our company is growing and we will be expanding our product line within the year to include hand and body balms, as well as other similar items and we will eventually have a few different product lines marketed at various age groups as well. Our lip balm is currently marketed to 14 to 40+ demographic, with the average age being roughly in the 15 to 24 range and our lip balm has been purchased by more women than men, though we market to both.

As far as software goes, I would like it to be in a format that is most popular- my old logo and graphics were made in Adobe Creative Suite 5.0, Adobe InDesign, and Adobe Illustrator, so the label should be made using this software (or a higher version). If I can have the label in a JPEG format also so I personally can add it to my website and social media that would be great.

I have a label redesign doc in an indd format but it was too large to upload. I believe this was the entire layout of our last label. If you need this, or anything else, please let me know as well as how I can send it to you.

We have applied to the popular TV show Otter Court and recently received a call back with interest from the producers; we are so excited and hope you are as well!

Thank you!
Gregor Tallowby
Owner
Petal Wrens Salves LLC
Gregor@PetalWrensSalves.example

The Label dimensions are: 2.25 inches wide ---> by 2 inches long. Currently, there is a .75 inch area that is part of the label and is perforated, used as a safety seal. I may be changing the labels to a slightly different kind but the dimensions will be the same. The tubes we use are standard lip balm tubes with a net weight of .15 ounces ( the total length of the tube from the bottom turning piece to the top of the cap is just over 2.5 inches (this is NOT how large the label must be).We are discontinuing the 1 Hive, 2 Hive concepts ( for different consistencies of the balm) so that part of the label does not need to be included.Feel free to enhance and/or modify the logo to fit the design of the label.Thank you! Added Thursday, February 12, 2015

Requirements
Must have
• Label Dimensions:
• Length: 2.125" Height: 2.125"
• Top Margin: 1.025" Bottom Margin: 1.025"
• Left Margin: 0.9125" Right Margin: 0.9125"
• Horizontal Spacing: 0.15" Vertical Spacing: 0.15"
• Horizontal Pitch: 2.275" Vertical Pitch: 2.275"

```html
<!DOCTYPE html>
<html lang="en">
<head>
<meta charset="utf-8">
<title>Trindle Salve – Lip Balm Label</title>
<link href="https://fonts.googleapis.com/css2?family=Montserrat:wght@400;500;600;700&display=swap" rel="stylesheet">
<style>
  :root {
    --stage: #e6e6e6;
    --label: #ffffff;
    --orange: #f5a01d;
    --orange-text: #f29a1f;
    --burgundy: #8b1f33;
    --honey-wash: #fcefdc;
    --white: #ffffff;
  }
  * { margin: 0; padding: 0; box-sizing: border-box; }
  html, body {
    width: 1200px; height: 857px; overflow: hidden;
  }
  body {
    background: radial-gradient(ellipse at center, #f7f7f7 0%, var(--stage) 75%);
    font-family: "Montserrat", sans-serif;
    position: relative;
  }
  .label {
    position: absolute; left: 225px; top: 53px;
    width: 750px; height: 750px;
    background: var(--label);
    box-shadow: 0 2px 6px rgba(0,0,0,0.18);
    overflow: hidden;
  }
  .honey-backdrop {
    position: absolute; left: 0; top: 0; width: 645px; height: 750px;
    background:
      radial-gradient(ellipse 70% 22% at 40% 47%, var(--honey-wash) 0%, rgba(252,239,220,0) 100%),
      linear-gradient(180deg, #fffaf3 0%, #fdf3e6 50%, #fffaf3 100%);
  }
  .mark-dot {
    position: absolute; border-radius: 50%; background: var(--orange);
  }
  .brand-name {
    position: absolute; color: var(--orange);
    font-weight: 500; letter-spacing: -1px; line-height: 0.95;
  }
  .brand-name--hero { left: 33px; top: 195px; font-size: 78px; }
  .maker-name {
    position: absolute; color: var(--burgundy);
    font-weight: 500; font-size: 30px; white-space: nowrap;
  }
  .product-type {
    position: absolute; color: var(--orange-text);
    font-weight: 700; text-align: center;
    border-top: 2px solid var(--orange); border-bottom: 2px solid var(--orange);
  }
  .product-type--top {
    left: 388px; top: 240px; width: 232px;
    font-size: 19px; padding: 3px 0 2px;
  }
  .flavor-pill {
    position: absolute; left: 387px; top: 292px; width: 235px; height: 40px;
    border-radius: 20px; background: var(--orange); color: var(--white);
    font-weight: 700; font-size: 17px;
    display: flex; align-items: center; justify-content: center;
  }
  .copy {
    position: absolute; color: var(--orange-text); text-align: justify;
  }
  .copy--ingredients {
    left: 230px; top: 430px; width: 393px;
    font-size: 12.4px; font-weight: 600; line-height: 17.3px;
  }
  .copy--ingredients strong { font-weight: 700; }
  .copy--secondary {
    left: 230px; top: 511px; width: 393px;
    font-size: 10.3px; font-weight: 500; line-height: 14.2px;
  }
  .copy--side {
    left: 33px; top: 588px; width: 209px;
    font-size: 10.3px; font-weight: 500; line-height: 14.4px;
  }
  .brand-lockup {
    position: absolute; left: 267px; top: 624px; width: 140px;
    text-align: center;
  }
  .brand-lockup .brand-name {
    position: static; font-size: 23px; letter-spacing: -0.5px;
    white-space: nowrap; padding-bottom: 5px;
    border-bottom: 2px solid var(--orange);
  }
  .brand-lockup .product-type {
    position: static; border: none; font-size: 12.6px; padding-top: 4px;
    white-space: nowrap;
  }
  .barcode-area {
    position: absolute; left: 428px; top: 587px; width: 194px; height: 120px;
    background: var(--orange); color: var(--white);
    font-weight: 700; font-size: 24px;
    display: flex; align-items: center; justify-content: center;
  }
  .seal-strip {
    position: absolute; left: 645px; top: 0; width: 105px; height: 750px;
    background: var(--orange);
    display: flex; flex-direction: column; align-items: center;
    justify-content: space-around; padding: 18px 0;
  }
  .seal-strip__name {
    writing-mode: vertical-rl;
    color: var(--white); font-weight: 500; font-size: 33px;
    letter-spacing: -0.5px; line-height: 1; white-space: nowrap;
  }
</style>
</head>
<body>
  <main class="label">
    <div class="honey-backdrop" role="img" aria-label="Faint honeycomb pattern background"></div>

    <span class="mark-dot" style="left:130px; top:55px; width:100px; height:100px;"></span>
    <div class="brand-name brand-name--hero">Trindle<br>Salve</div>

    <span class="mark-dot" style="left:480px; top:80px; width:70px; height:70px;"></span>
    <div class="maker-name" style="left:432px; top:163px;">Petal Wrens</div>

    <div class="product-type product-type--top">BEESWAX LIP BALM</div>
    <div class="flavor-pill">Brown Sugar Cookie</div>

    <span class="mark-dot" style="left:110px; top:425px; width:70px; height:70px;"></span>
    <div class="maker-name" style="left:40px; top:515px; font-size:28px;">Petal Wrens</div>

    <p class="copy copy--ingredients"><strong>INGREDIENTS:</strong> Lorem ipsum dolor sit amet, consectetur adipisicing elit, sed do eiusmod tempor incididunt ut labore et dolore magna aliqua. Ut enim ad minim veniam, quis nostrud exercitation.</p>

    <p class="copy copy--secondary">Lorem ipsum dolor sit amet, consectetur adipisicing elit, sed do eiusmod tempor incididunt ut labore et dolore magna aliqua. Ut enim ad minim veniam, quis nostrud exercitation.</p>

    <p class="copy copy--side">Lorem ipsum dolor sit amet, consectetur adipisicing elit, sed do eiusmod tempor incididunt ut labore et dolore magna aliqua. Ut enim ad minim veniam, quis nostrud exercitation. Lorem ipsum dolor sit amet, consectetur adipisicing elit, sed do.</p>

    <div class="brand-lockup">
      <div class="brand-name">Trindle Salve</div>
      <div class="product-type">BEESWAX LIP BALM</div>
    </div>

    <div class="barcode-area">BARCODE</div>

    <aside class="seal-strip">
      <div class="seal-strip__name">Trindle Salve</div>
      <div class="seal-strip__name">Trindle Salve</div>
      <div class="seal-strip__name">Trindle Salve</div>
    </aside>
  </main>
</body>
</html>
```